Website for a company offering full serivce charging solutions for electric cars

The company "mero-kant" (english: "mero-edge") offering all-in-one-solutions for charging infrastructure for electric mobility.

There are four products:
1- Wallboxes for single-family homes
2- Solutions for property devloper/-management for property parking space
3- All-in-one-charging solution for municipalities/communities
4- Solutions for tourism/hotels/holiday appartments

The Website structure:
1. Main Page
2.1. Product Page Single Homes
2.2. Product Page Property Management / Parking
2.3. Product Page Municipality
2.4. Product Page Tourism
3. Contact Form / Request for information
4. Imprint / Legal

The Website should be built on Wordpress with a powerful possibility to simply add/modify specific landing pages.

We would like you to implement the website later and also maintain it if possible, but we would be able to do minor modifications by ourselfs (for A/B-Testing)

The website should be clear and simple, easy to understand.
Target group is mainly B2C without deeper knowledge of that topic.

It should suggest, that we will provide a very simple way to get the charging infrastructure done.

We need a contact form, maybe we will use Hubspot later.

Attached you will find a draft of the main page and a landing page (for 2.2) - it is just the content, please ignore the design. We would love to let you create a suitable design.
Also you will find some drafts a bit different for the same story.

I added also a few stock photos, but they don't need to be used! If you have better ideas, you are welcome!

Industry/Entity Type

Charging/Electric mobility

Number of Pages Required

2 page

Font styles to use
Sans Serif

Requirements
Must have
• Based on Wordpress, and the designer should be able to implement it on Wordpress on a later step

```html
<!DOCTYPE html>
<html lang="de">
<head>
<meta charset="utf-8">
<title>mero-kant – Ladelösungen aus einer Hand</title>
<link href="https://fonts.googleapis.com/css2?family=Playfair+Display:wght@400;700&family=Lato:wght@400;700&display=swap" rel="stylesheet">
<style>
:root{
  --magenta:#c43ab9;
  --violet:#7550c8;
  --ink:#1c1c1c;
  --nav:#555;
  --hero-bg:#ecf1f4;
  --dark:#0b0d18;
  --footer:#050505;
  --white:#fff;
}
*{box-sizing:border-box;margin:0;padding:0}
html,body{width:1200px;height:2295px;overflow:hidden}
body{position:relative;background:var(--white);font-family:"Playfair Display",serif;color:var(--ink)}
.site-header{position:absolute;top:0;left:0;width:1200px;height:81px}
.brand{position:absolute;left:101px;top:29px;display:flex;align-items:center;gap:8px;font-size:22px;font-weight:400;color:var(--ink)}
.brand-dot{width:14px;height:14px;border-radius:50%;background:var(--magenta)}
.main-nav{position:absolute;left:545px;top:38px;display:flex;gap:18px;font-size:15px;color:var(--nav)}
.call-button{position:absolute;left:951px;top:32px;width:147px;height:30px;border-radius:4px;background:linear-gradient(90deg,var(--magenta),var(--violet));color:var(--white);font-family:"Lato",sans-serif;font-size:15px;display:flex;align-items:center;justify-content:center;gap:5px}
.section{position:absolute;left:0;width:1200px}
.hero{top:81px;height:517px;background:var(--hero-bg)}
.gradient-title{font-weight:700;background:linear-gradient(90deg,var(--magenta),var(--violet));-webkit-background-clip:text;background-clip:text;color:transparent;font-size:27px}
.hero-copy{position:absolute;left:99px;top:70px;width:500px}
.hero-sub{font-size:18px;font-weight:700;line-height:21px;margin:10px 0 22px}
.hero-copy p{font-size:13.5px;line-height:18px;margin-bottom:18px}
.photo{position:absolute}
.hero-photo{left:612px;top:34px;width:496px;height:422px;background:linear-gradient(160deg,#e8a84a 0%,#b97a3d 30%,#4a4237 60%,#cfd3d4 100%)}
.private-photo{left:92px;top:658px;width:495px;height:423px;background:linear-gradient(135deg,#2f6ea6 0%,#9fbfd8 45%,#e6eef4 70%,#a9c2d6 100%)}
.municipal-photo{left:609px;top:1688px;width:495px;height:423px;background:linear-gradient(135deg,#1c57c9 0%,#7fb0f0 45%,#e6eefb 65%,#3a73d8 100%)}
.feature-block{position:absolute}
.checklist{list-style:none;font-size:13.5px;line-height:18px}
.checklist>li{position:relative;padding-left:21px;margin-bottom:12px}
.checklist>li::before{content:"";position:absolute;left:3px;top:4px;width:5px;height:9px;border-right:2.4px solid currentColor;border-bottom:2.4px solid currentColor;transform:rotate(40deg)}
.sublist{list-style:none;margin-top:4px;line-height:21.5px}
.sublist li{position:relative;padding-left:9px}
.sublist li::before{content:"";position:absolute;left:0;top:7px;border-left:4px solid currentColor;border-top:4px solid transparent;border-bottom:4px solid transparent}
.private-block{left:607px;top:707px;width:510px}
.private-block h2{margin-bottom:14px}
.business{top:1173px;height:467px}
.business-left{position:absolute;left:0;top:0;width:600px;height:467px;background:radial-gradient(circle at 30% 30%,#d06ad0 0%,#b24fb8 50%,#9a3fa8 100%);color:var(--white)}
.business-right{position:absolute;left:600px;top:0;width:600px;height:467px;background:linear-gradient(135deg,#1e2130 0%,#0b0d18 50%,#02030a 100%);color:var(--white)}
.business-left h2{position:absolute;left:111px;top:80px;font-size:27px;font-weight:700}
.business-left .checklist{position:absolute;left:96px;top:148px;width:500px;line-height:18px}
.business-left .checklist>li{margin-bottom:6px}
.business-right .checklist{position:absolute;left:22px;top:142px;width:530px}
.business-right .checklist>li{margin-bottom:11px}
.municipal-block{left:92px;top:1720px;width:515px}
.municipal-block h2{margin-left:3px;margin-bottom:14px}
.municipal-block .checklist>li{margin-bottom:11px}
.site-footer{position:absolute;left:0;top:2227px;width:1200px;height:68px;background:var(--footer);color:var(--white);font-size:14px}
.copyright{position:absolute;left:99px;top:26px}
.footer-nav{position:absolute;left:459px;top:24px;display:flex;gap:7px}
.footer-nav span.sep{opacity:.8}
.social{position:absolute;left:980px;top:14px;display:flex;gap:8px}
.social span{width:38px;height:38px;border-radius:50%;background:#d8d8d8}
</style>
</head>
<body>
<header class="site-header">
  <div class="brand"><span class="brand-dot"></span>mero-kant.de</div>
  <nav class="main-nav"><span>Lösungen</span><span>Unternehmen</span><span>Services</span><span>Karriere</span><span>Kontakt</span></nav>
  <div class="call-button"><svg width="12" height="12" viewBox="0 0 24 24"><path fill="#fff" d="M6.6 10.8a15.1 15.1 0 0 0 6.6 6.6l2.2-2.2a1 1 0 0 1 1-.25 11.4 11.4 0 0 0 3.6.57 1 1 0 0 1 1 1V20a1 1 0 0 1-1 1A17 17 0 0 1 3 4a1 1 0 0 1 1-1h3.5a1 1 0 0 1 1 1c0 1.25.2 2.45.57 3.57a1 1 0 0 1-.25 1z"/></svg>(555) 010-4827</div>
</header>

<section class="section hero">
  <div class="hero-copy">
    <h1 class="gradient-title">mero-kant ist Ihr Partner</h1>
    <p class="hero-sub">wenn das Laden nicht nur einfach, sondern die Umsetzung auch aus einer Hand kommen soll</p>
    <p>Wir bieten Lösungen sowohl für Privatkunden, Geschäftskunden als auch Kommunen an, die schnell, fair und ohne Eigenleistung zu einer smarten Ladelösung für E-Fahrzeuge kommen möchten.</p>
    <p>Von der Beratung, über die Installation, Inbetriebnahme bis zur Abrechnung und Wartung bekommen Sie bei mero-kant alles aus einer Hand. Auf Wunsch vermieten wir auch die Ladetechnik und übernehmen im gewerblichen Bereich die direkte Abrechnung mit dem Nutzer. Für Kommunen bieten wir den kostenfreien Full-Service an und beteiligen die Gemeinden an der Nutzung der Infrastruktur.</p>
    <p>Fragen Sie uns nach der auf Ihre individuellen Bedürfnisse zugeschnittenen Lösung</p>
  </div>
  <div class="photo hero-photo" role="img" aria-label="Frau mit Smartphone neben einem Elektroauto an der Ladestation bei Sonnenuntergang"></div>
</section>

<div class="photo private-photo" role="img" aria-label="Ladestecker in der Buchse eines hellen Elektroautos"></div>
<div class="feature-block private-block">
  <h2 class="gradient-title">als Privatkunde</h2>
  <ul class="checklist">
    <li>Bestandsanalyse mit umfangreicher Beratung über die Möglichkeiten der Umsetzung</li>
    <li>Prüfung und Übernahme der Anmeldung verfügbarer Fördermöglichkeiten</li>
    <li>Auswahl an smarten Wallbox Lösungen, passend für Ihr Fahrzeug und Ihre Bedürfnisse</li>
    <li>Installation inkl. aller notwendigen Materialien und Tätigkeiten (Durchbrüche, Erdarbeiten, etc.)</li>
    <li>Inbetriebnahme und Einweisung in die Ladetechnik</li>
    <li>Jährlich technische Wartung nach DGUV3</li>
    <li>Reparaturservice, unter Berücksichtigung der geltenden Garantie Ansprüche</li>
  </ul>
</div>

<section class="section business">
  <div class="business-left" role="img" aria-label="Ladestecker vor unscharfem Lichterhintergrund in Magenta">
    <h2>als Geschäftskunde</h2>
    <ul class="checklist">
      <li>Durchführung einer individuellen Bedarfsanalyse inkl. Ermittlung der Anforderungen für:
        <ul class="sublist">
          <li>Haus- und Immobilienverwaltungen</li>
          <li>Dienstleistungs- und Handelsunternehmen</li>
          <li>Hotel und Beherbergungsbetriebe</li>
          <li>Parkraum- und Parkhausbetreiber</li>
          <li>Tourismus, Sport- und Freizeiteinrichtungen</li>
        </ul>
      </li>
      <li>Planung und Projektierung des Installationsaufwands inkl. Materialverbrauch</li>
      <li>Leasing oder Kauf der Hardware</li>
      <li>Normgerechte Installation der Ladeinfrastruktur inkl. Durchbruch-, Brandschutz- und Erdarbeiten</li>
    </ul>
  </div>
  <div class="business-right" role="img" aria-label="Dunkle Ladesäule mit Bedienfeld">
    <ul class="checklist">
      <li>Bei Bestandsbauten Integration der Ladeinfrastruktur in die Gebäudesystemtechnik und ggf. Anpassung des Netzanschlusses</li>
      <li>Inbetriebnahme der Anlage inkl. Prüf- und Messprotokollen</li>
      <li>Wiederkehrende technische Prüfung der Anlage nach DGUV 3</li>
      <li>Austausch und Reparatur Service</li>
      <li>Unterstützung bei der mtl. Nutzungsabrechnung und Einbindung in Ihre vorhandene Abrechnungssysteme</li>
      <li>ODER direkte Abrechnung mit den Nutzern</li>
    </ul>
  </div>
</section>

<div class="feature-block municipal-block">
  <h2 class="gradient-title">als Kommune</h2>
  <ul class="checklist">
    <li>Konzeptionierung möglicher Ladeinfrastrukturen innerhalb Ihrer Gemeinde</li>
    <li>Planung und Projektsteuerung inkl. sämtlicher behördlicher Genehmigungsverfahren und Beantragung von Fördermitteln</li>
    <li>Fachgerechte Installation und Inbetriebnahme</li>
    <li>Regelmäßige Wartung gemäß Vorschrif</li>
    <li>Reparatur und Kundenservice</li>
    <li>Direkte Abrechnung mit dem Nutzer</li>
    <li>Beteiligung der Gemeinde am Umsatz</li>
    <li>Möglichkeit der Integration von Bonusprogrammen, mit denen der lokale Einzelhandel beworben wird</li>
  </ul>
</div>
<div class="photo municipal-photo" role="img" aria-label="Leuchtend blaue Ladebuchse an einem weißen Elektroauto"></div>

<footer class="site-footer">
  <div class="copyright">©mero-kant GmbH</div>
  <nav class="footer-nav"><span>AGB</span><span class="sep">|</span><span>Datenschutzerklärung</span><span class="sep">|</span><span>Impressum</span><span class="sep">|</span><span>Kontakt</span><span class="sep">|</span><span>Karriere</span><span class="sep">|</span><span>FAQs</span></nav>
  <div class="social"><span></span><span></span><span></span></div>
</footer>
</body>
</html>
```